Price Comparison Homepage

We are a price comparison service. I would like a concept page for a new homepage for our financial comparison service. Current homepage can be found at www.coinlantern.com.hk/en

I have also attached another concept which includes the sample content we
would like to include on the concept...

Note: The footer area (from "why choose coinlantern" down) is fixes as is
the header (menu).

The new colours are shown in the attachment, we are moving away from the
green and to the blue attached.

Financial

```html
<!DOCTYPE html>
<html lang="en">
<head>
<meta charset="utf-8">
<title>CoinLantern – Compare and Save</title>
<link href="https://fonts.googleapis.com/css2?family=Open+Sans:wght@400;600;700&display=swap" rel="stylesheet">
<style>
:root{
  --blue:#0b6a9a;
  --blue-dark:#08557d;
  --navy:#0f3f5c;
  --title-blue:#1b7cab;
  --orange:#f7941d;
  --green:#6aab3d;
  --grey-bg:#f3f3f3;
  --text:#333;
  --muted:#666;
  --white:#fff;
}
*{box-sizing:border-box;margin:0;padding:0}
html,body{width:1200px;height:3061px;overflow:hidden}
body{font-family:"Open Sans",Arial,sans-serif;color:var(--text);background:var(--white);position:relative}
.wrap{width:980px;margin:0 auto;position:relative}
a{color:inherit;text-decoration:none}

/* header */
.site-header{height:65px}
.site-header .wrap{display:flex;align-items:center;height:65px}
.brand{display:flex;align-items:center;gap:10px;font-weight:700;font-size:26px;color:var(--blue)}
.brand-dot{width:18px;height:18px;border-radius:50%;background:var(--blue)}
.main-nav{margin-left:auto;display:flex;font-size:13px}
.main-nav a{padding:0 10px;border-left:1px solid #333;line-height:14px}
.main-nav a:first-child{border-left:0;color:var(--title-blue)}
.country{margin-left:20px;border:1px solid #ccc;border-radius:3px;font-size:11px;padding:4px 8px;display:flex;align-items:center;gap:6px}
.country .flag{width:18px;height:11px;background:linear-gradient(#2c4fa0 50%,#c8283a 50%)}

/* hero */
.hero{height:252px;background:radial-gradient(ellipse at 30% 40%,#1a8ad0 0%,#0a5596 45%,#06305e 100%);position:relative}
.hero .wrap{height:252px}
.hero-figure{position:absolute;left:0;top:25px;width:190px;height:210px;border-radius:40% 40% 10% 10%;background:linear-gradient(#7bb944,#4e8b2c)}
.hero-copy{position:absolute;left:238px;top:22px;color:var(--white)}
.hero-copy h1{font-weight:400;font-size:38px}
.hero-copy p{font-size:21px;margin-top:2px}
.btn{display:inline-block;background:var(--orange);color:var(--white);font-weight:600;text-transform:uppercase}
.hero-copy .btn{font-size:12px;padding:10px 18px;margin-top:14px}
.dots{position:absolute;left:238px;top:224px;display:flex;gap:6px}
.dots i{width:8px;height:8px;border-radius:50%;background:var(--white)}
.dots i:first-child{background:none;border:1px solid var(--white)}
.side-tabs{position:absolute;right:0;top:100px}
.side-tabs span{display:block;width:38px;height:26px;background:var(--green);margin-bottom:8px;border-radius:4px 0 0 4px}

/* tabs */
.product-tabs{position:absolute;top:317px;left:110px;width:980px;height:83px;display:flex;background:var(--blue);z-index:2}
.product-tabs a{flex:1;display:flex;align-items:center;justify-content:center;gap:12px;color:var(--white);font-size:13px;border-left:1px solid #0a5f88}
.product-tabs a.active{background:var(--green);position:relative}
.product-tabs a.active::after{content:"";position:absolute;bottom:-12px;left:50%;margin-left:-10px;border:10px solid transparent;border-top-color:var(--green);border-bottom:0}

/* finder */
.finder{background:var(--grey-bg);height:407px;text-align:center;padding-top:104px}
.finder h2{color:var(--title-blue);font-weight:400;font-size:31px;line-height:42px}
.finder .sub{font-size:16px;line-height:22px}
.selects{display:flex;justify-content:center;gap:35px;margin-top:45px}
.select{width:411px;height:53px;background:var(--white);border:1px solid #ddd;display:flex;align-items:center;justify-content:space-between;padding:0 18px;font-size:12px}
.select::after{content:"";border:7px solid transparent;border-top-color:#333;border-bottom:0}
.finder-action{margin-top:19px;height:51px}
.finder .btn{font-size:17px;line-height:23px;padding:14px 24px;font-weight:400}
.help{display:flex;justify-content:center;gap:50px;margin-top:21px;font-size:16px;line-height:22px;color:var(--navy)}
.help span{display:flex;align-items:center;gap:8px}

/* partners */
.partners{height:92px;display:flex;justify-content:center;align-items:center;gap:70px;font-weight:700;font-size:20px;color:#777;box-shadow:0 10px 14px -10px rgba(0,0,0,.12);position:relative}

/* products */
.products{background:#fafafa;padding:37px 0 54px}
.product-grid{display:grid;grid-template-columns:repeat(3,309px);gap:25px 26px}
.product-card{background:var(--blue);color:var(--white);height:341px;padding:26px 22px}
.card-head{display:flex;align-items:center;gap:14px}
.card-head h3{font-weight:400;font-size:25px;line-height:26px}
.ic{width:44px;height:44px;border:3px solid var(--white);border-radius:50%;display:flex;align-items:center;justify-content:center;flex:none}
.product-card ul{list-style:none;margin-top:26px}
.product-card li{font-size:12px;line-height:21px;padding-left:24px;position:relative;margin-bottom:18px}
.product-card li::before{content:"";position:absolute;left:0;top:4px;width:12px;height:12px;border-radius:50%;background:var(--white)}
.product-card li::after{content:"";position:absolute;left:3px;top:7px;border:3px solid transparent;border-left:5px solid var(--blue)}
.product-card .btn{font-size:12px;padding:8px 13px;margin-top:2px}

/* why */
.why{background:var(--grey-bg);height:235px;text-align:center;padding-top:44px}
.why h2{font-weight:400;font-size:31px;color:var(--navy)}
.why h2 span{color:var(--title-blue)}
.why-list{display:flex;justify-content:space-between;margin-top:44px;padding:0 10px}
.why-item{display:flex;align-items:center;gap:30px;font-size:20px;text-align:left;line-height:27px;color:#333}

/* testimonials */
.testimonials{background:var(--blue);height:399px;color:var(--white);text-align:center;padding-top:26px}
.testimonials h2{font-weight:400;font-size:30px}
.avatar{width:154px;height:154px;border-radius:50%;margin:20px auto 0;background:radial-gradient(circle at 50% 45%,#e9c99a,#d9a93a 70%)}
.quote-mark{position:absolute;left:0;top:212px}
.testimonials blockquote{font-size:15px;line-height:30px;margin-top:32px}
.testimonials cite{display:block;font-style:normal;font-weight:600;font-size:20px;margin-top:14px}
.testimonials .loc{font-size:14px}

/* steps */
.steps{height:384px;text-align:center;padding-top:36px}
.steps h2{color:var(--title-blue);font-weight:400;font-size:31px}
.steps .intro{font-size:16px;line-height:28px;color:#444;margin-top:18px}
.step-grid{display:grid;grid-template-columns:repeat(3,309px);gap:26px;margin-top:30px;text-align:center}
.step{background:var(--blue);color:var(--white);height:178px;padding-top:20px}
.step svg{display:block;margin:0 auto}
.step-shadow{width:110px;height:8px;margin:4px auto 0;border-radius:50%;background:rgba(0,0,0,.2)}
.step h3{font-size:22px;font-weight:600;margin-top:10px}
.step p{font-size:16px}

/* newsletter */
.newsletter{background:var(--navy);height:98px}
.newsletter .wrap{display:flex;align-items:center;height:98px}
.newsletter h3{color:var(--white);font-weight:400;font-size:26px;margin-left:20px;width:290px}
.newsletter .field{width:420px;height:56px;background:#0b2a3e;border:1px solid #1d5878;color:var(--white);font-size:15px;display:flex;align-items:center;padding-left:18px}
.newsletter .btn{height:56px;line-height:56px;padding:0 18px;font-size:20px;text-transform:none;font-weight:400;margin-left:14px}

/* footer */
.site-footer{padding-top:52px;height:233px;border-bottom:1px solid #ddd}
.footer-cols{display:flex;padding-left:28px}
.footer-col{width:254px}
.footer-col:nth-child(2){width:200px}
.footer-col:nth-child(3){width:268px}
.footer-col h4{color:var(--title-blue);font-weight:400;font-size:16px;margin-bottom:14px}
.footer-col a{display:block;font-size:13px;margin-bottom:18px}
.social{display:flex;gap:8px}
.social span{width:18px;height:18px;background:#2d6f8f;border-radius:2px}
.bottom-bar{text-align:center;padding-top:16px;font-size:12px}
.bottom-links a{padding:0 9px;border-left:1px solid #333}
.bottom-links a:first-child{border-left:0}
.copyright{margin-top:16px}
</style>
</head>
<body>

<header class="site-header">
  <div class="wrap">
    <div class="brand"><span class="brand-dot"></span>CoinLantern</div>
    <nav class="main-nav">
      <a href="#">Credit Card</a><a href="#">Personal Loan</a><a href="#">Health Insurance</a><a href="#">Mortage</a><a href="#">Travel Insurance</a>
    </nav>
    <div class="country"><span class="flag"></span>Philippines ▾</div>
  </div>
</header>

<section class="hero">
  <div class="wrap">
    <div class="hero-figure" role="img" aria-label="Illustrated mascot in a green superhero suit giving a thumbs up"></div>
    <div class="hero-copy">
      <h1>The Best Way to Compare and save...</h1>
      <p>Credit Cards ,Broadband,Loans and insurance</p>
      <a class="btn" href="#">Get Started</a>
    </div>
    <div class="dots"><i></i><i></i><i></i><i></i></div>
  </div>
  <div class="side-tabs"><span></span><span></span></div>
</section>

<nav class="product-tabs">
  <a class="active" href="#"><svg width="22" height="16" viewBox="0 0 22 16"><rect x="1" y="1" width="20" height="14" rx="2" fill="none" stroke="#fff" stroke-width="2"/><rect x="1" y="4" width="20" height="3" fill="#fff"/></svg>Credit Cards</a>
  <a href="#"><svg width="12" height="20" viewBox="0 0 12 20"><text x="1" y="16" fill="#fff" font-size="18" font-family="Open Sans,sans-serif" font-weight="700">$</text></svg>Rollover loans</a>
  <a href="#"><svg width="24" height="18" viewBox="0 0 24 18"><path d="M3 9 L6 2 H18 L21 9 V15 H3Z" fill="#fff"/><circle cx="7" cy="12" r="2" fill="#0b6a9a"/><circle cx="17" cy="12" r="2" fill="#0b6a9a"/></svg>Car Insurance</a>
  <a href="#"><svg width="22" height="18" viewBox="0 0 22 18"><path d="M1 6a14 14 0 0 1 20 0M4 9.5a9 9 0 0 1 14 0M7.5 13a4 4 0 0 1 7 0" fill="none" stroke="#fff" stroke-width="2.2"/><circle cx="11" cy="16" r="1.8" fill="#fff"/></svg>Broadband</a>
</nav>

<section class="finder">
  <h2>Find Your perfect credit card in seconds</h2>
  <p class="sub">Apply through us and get online application rewards 100% free and impartial</p>
  <div class="selects">
    <div class="select">Which Banks ?</div>
    <div class="select">Which Card Types ?</div>
  </div>
  <div class="finder-action"><a class="btn" href="#">Compare Now</a></div>
  <div class="help">
    <span><svg width="14" height="14" viewBox="0 0 14 14"><circle cx="7" cy="7" r="7" fill="#0f3f5c"/><text x="4" y="11" fill="#fff" font-size="10" font-weight="700" font-family="Open Sans,sans-serif">?</text></svg>Help me select a card</span>
    <span><svg width="14" height="14" viewBox="0 0 14 14"><rect width="14" height="14" rx="2" fill="#0f3f5c"/><path d="M4 3c-1 1 0 5 3 7s4 1 4 0l-2-2-1 1C7 8 6 7 5 5l1-1z" fill="#fff"/></svg>Call Us On 09170 555 0142</span>
  </div>
</section>

<section class="partners">
  <span>Northbay</span><span>Pacifica</span><span>Metrovale</span><span>Islandic</span><span>Cityward</span><span>Harborline</span>
</section>

<section class="products">
  <div class="wrap product-grid">
    <article class="product-card">
      <div class="card-head"><span class="ic"><svg width="22" height="18" viewBox="0 0 22 18"><path d="M2 6h12v8H2zM14 9h4l3 3v2h-7z" fill="#fff"/><path d="M6 8v4M4 10h4" stroke="#0b6a9a" stroke-width="1.6"/></svg></span><h3>Health<br>Insurance</h3></div>
      <ul><li>Save money by paying the lowest monthly premiums</li><li>Speak to our friendly advisors to find personalised health insurance solutions</li><li>100% free and impartial</li></ul>
      <a class="btn" href="#">Compare Now</a>
    </article>
    <article class="product-card">
      <div class="card-head"><span class="ic"><svg width="22" height="20" viewBox="0 0 22 20"><path d="M11 1 21 10h-3v9H4v-9H1z" fill="#fff"/><rect x="9" y="12" width="4" height="7" fill="#0b6a9a"/></svg></span><h3>Mortgage</h3></div>
      <ul><li>Save money by paying the lowest monthly premiums</li><li>Speak to our friendly advisors to find personalised health insurance solutions</li><li>100% free and impartial</li></ul>
      <a class="btn" href="#">Compare Now</a>
    </article>
    <article class="product-card">
      <div class="card-head"><span class="ic"><svg width="20" height="22" viewBox="0 0 20 22"><rect x="2" y="1" width="16" height="16" rx="3" fill="#fff"/><rect x="4" y="4" width="12" height="6" fill="#0b6a9a"/><circle cx="6" cy="13" r="1.5" fill="#0b6a9a"/><circle cx="14" cy="13" r="1.5" fill="#0b6a9a"/><path d="M4 17l-2 4M16 17l2 4" stroke="#fff" stroke-width="2"/></svg></span><h3>Travel<br>Insurance</h3></div>
      <ul><li>Save money by paying the lowest monthly premiums</li><li>Speak to our friendly advisors to find personalised health insurance solutions</li><li>100% free and impartial</li></ul>
      <a class="btn" href="#">Compare Now</a>
    </article>
    <article class="product-card">
      <div class="card-head"><span class="ic"><svg width="22" height="16" viewBox="0 0 22 16"><rect x="1" y="1" width="20" height="14" rx="2" fill="none" stroke="#fff" stroke-width="2"/><rect x="1" y="4" width="20" height="3" fill="#fff"/></svg></span><h3>Credit Card<br>Guide</h3></div>
      <ul><li>Save money by paying the lowest monthly premiums</li><li>Speak to our friendly advisors to find personalised health insurance solutions</li><li>100% free and impartial</li></ul>
      <a class="btn" href="#">Compare Now</a>
    </article>
    <article class="product-card">
      <div class="card-head"><span class="ic"><svg width="20" height="20" viewBox="0 0 20 20"><circle cx="10" cy="6" r="4.5" fill="#fff"/><path d="M2 19c0-5 4-7 8-7s8 2 8 7z" fill="#fff"/></svg></span><h3>Personal Loan<br>Guide</h3></div>
      <ul><li>Save money by paying the lowest monthly premiums</li><li>Speak to our friendly advisors to find personalised health insurance solutions</li><li>100% free and impartial</li></ul>
      <a class="btn" href="#">Compare Now</a>
    </article>
    <article class="product-card">
      <div class="card-head"><span class="ic"><svg width="20" height="20" viewBox="0 0 20 20"><path d="M5 2h12v14l-3 3H3V4z" fill="#fff"/><path d="M7 7h7M7 10h7M7 13h5" stroke="#0b6a9a" stroke-width="1.5"/></svg></span><h3>Health Insurance<br>Guide</h3></div>
      <ul><li>Save money by paying the lowest monthly premiums</li><li>Speak to our friendly advisors to find personalised health insurance solutions</li><li>100% free and impartial</li></ul>
      <a class="btn" href="#">Compare Now</a>
    </article>
  </div>
</section>

<section class="why">
  <h2>Why Choose <span>Coin Lantern</span></h2>
  <div class="wrap why-list">
    <div class="why-item"><svg width="30" height="34" viewBox="0 0 30 34"><rect x="2" y="2" width="26" height="30" rx="2" fill="none" stroke="#0b6a9a" stroke-width="3"/><rect x="6" y="6" width="18" height="6" fill="#0b6a9a"/><g fill="#0b6a9a"><rect x="6" y="15" width="4" height="4"/><rect x="13" y="15" width="4" height="4"/><rect x="20" y="15" width="4" height="4"/><rect x="6" y="22" width="4" height="4"/><rect x="13" y="22" width="4" height="4"/><rect x="20" y="22" width="4" height="4"/></g></svg><span>100% Impartial<br>100% Independent</span></div>
    <div class="why-item"><svg width="30" height="30" viewBox="0 0 30 30"><path d="M2 2h12l14 14-12 12L2 14z" fill="#0b6a9a"/><circle cx="8" cy="8" r="2.5" fill="#f3f3f3"/></svg><span>Free and Without<br>Obligation</span></div>
    <div class="why-item"><svg width="32" height="32" viewBox="0 0 32 32"><rect x="10" y="2" width="18" height="20" rx="2" fill="none" stroke="#0b6a9a" stroke-width="3"/><rect x="3" y="10" width="18" height="20" rx="2" fill="#f3f3f3" stroke="#0b6a9a" stroke-width="3"/></svg><span>Easy Market<br>Comparison</span></div>
  </div>
</section>

<section class="testimonials">
  <div class="wrap">
    <h2>Testimonials</h2>
    <div class="avatar" role="img" aria-label="Portrait photo of a smiling customer in a yellow top"></div>
    <svg class="quote-mark" width="30" height="24" viewBox="0 0 30 24"><path d="M2 22V12C2 5 6 2 12 1v5c-3 1-4 3-4 6h4v10zM18 22V12c0-7 4-10 10-11v5c-3 1-4 3-4 6h4v10z" fill="#fff"/></svg>
    <blockquote>Lorem Ipsum is simply dummy text of the printing and typesetting industry. Lorem Ipsum has been the industry's standard dummy text ever<br>since the 1500s, when an unknown printer took a galley of type and scrambled it to make a type specimen book.</blockquote>
    <cite>Daniel Reyes</cite>
    <div class="loc">London</div>
  </div>
</section>

<section class="steps">
  <h2>Compare then buy in 3 easy steps</h2>
  <p class="intro">Coinlantern helps you get what you need in 3easy steps .<br>You Can quote prices and compare all the features of various products</p>
  <div class="wrap step-grid">
    <div class="step"><svg width="46" height="56" viewBox="0 0 46 56"><path d="M2 2h28l14 14v38H2z" fill="#fff"/><path d="M30 2v14h14" fill="#d7e7ef"/><path d="M10 24h26M10 32h26M10 40h26" stroke="#0b6a9a" stroke-width="3"/></svg><div class="step-shadow"></div><h3>Step 1</h3><p>Fill in a form to recive instant results</p></div>
    <div class="step"><svg width="56" height="56" viewBox="0 0 56 56"><circle cx="22" cy="22" r="16" fill="none" stroke="#fff" stroke-width="7"/><path d="M34 34l18 18" stroke="#fff" stroke-width="9" stroke-linecap="round"/></svg><div class="step-shadow"></div><h3>Step 2</h3><p>Compare the products</p></div>
    <div class="step"><svg width="54" height="54" viewBox="0 0 54 54"><rect x="2" y="2" width="50" height="50" rx="8" fill="#fff"/><path d="M14 27l9 9 18-18" fill="none" stroke="#0b6a9a" stroke-width="7"/></svg><div class="step-shadow"></div><h3>Step 3</h3><p>Buy the best option for you</p></div>
  </div>
</section>

<section class="newsletter">
  <div class="wrap">
    <h3>Free Money Saving Tips</h3>
    <div class="field">Enter your E-mail ID</div>
    <a class="btn" href="#">Get Free Access Now !</a>
  </div>
</section>

<footer>
  <div class="site-footer">
    <div class="wrap footer-cols">
      <div class="footer-col"><h4>Credit Card</h4><a href="#">Credit Card Comparison</a><a href="#">Credit Card FAQ</a><a href="#">Credit Card Glossary</a><a href="#">Credit Card Guide</a></div>
      <div class="footer-col"><h4>Loan</h4><a href="#">Personal Loan Comparison</a><a href="#">Personal Loan Guide</a><a href="#">Mortgage</a></div>
      <div class="footer-col"><h4>Insurance</h4><a href="#">Health Insurance Comparison</a><a href="#">Travel Insurance Comparison</a></div>
      <div class="footer-col"><h4>Connect With Us</h4><div class="social"><span></span><span></span><span></span><span></span></div></div>
    </div>
  </div>
  <div class="bottom-bar">
    <div class="bottom-links"><a href="#">About</a><a href="#">Contact Us</a><a href="#">FAQs</a><a href="#">Product Guide</a><a href="#">Careers</a><a href="#">Terms &amp; Conditions and Privacy Policy</a><a href="#">Glossary</a><a href="#">Affiliates</a><a href="#">Press</a><a href="#">Sitemap</a><a href="#">Blog</a></div>
    <p class="copyright">© 2013 - 2014 CoinLantern Global Limited. All rights reserved. Use of this site constitutes acceptance of our Terms of Use and Privacy Policy.</p>
  </div>
</footer>

</body>
</html>
```